Plastikfrei Buchdesign
Zielgruppe
Wir sind Buchautor und möchten ein hochwertiges Design. Unsere Zielgruppe sind besonders Mütter und Väter, die ihren Alltag durch plastikfreie Alternativen ergänzen möchten.
Aufgabenstellung
Das Coverformat beträgt 5,25x8 inch und das Taschenbuch hat 148 Seiten.
Titel: Sonnig kochen
Untertitel: Wie du durch Zero Waste die Umwelt nachhaltig von Abfall befreist und dein Leben ökologischer gestaltest- inkl. 30 Tage Wolkenretter Challenge
Der Haupttitel des Designs soll groß ersichtlich sein. So dass das Thema auch bei kleiner Auflösung in Werbeanzeigen gut ersichtlich ist. Weiterhin sollen auf dem Cover der Einfluss durch die Alternativen zum Plastik ersichtlich werden. Auch soll sichtbar werden, dass der Einfluss von jedem einzelnen etwas bringt.
Es wird benötigt:
Buchcover mit Buchrücken, Rückseite und für den Gewinner später noch eine quadratische Version fürs Hörbuch.
Die Textdatei im Anhang enthält ein paar Informationen für das Projekt generell und nur der Beschreibungstext soll schön formatiert ohne den Call To Action auf die Buchrückseite.

```html
<!DOCTYPE html>
<html lang="de">
<head>
<meta charset="utf-8">
<title>Sonnig kochen – Buchumschlag</title>
<link href="https://fonts.googleapis.com/css2?family=Montserrat:wght@600&family=Cabin:wght@500;600&display=swap" rel="stylesheet">
<style>
  :root {
    --paper: #f7f9f6;
    --title-red: #f40a0c;
    --title-green: #3bb01b;
    --ink: #3a3a3a;
    --sky-deep: #1f6fd0;
    --sky-light: #8fc2f0;
    --scene-green: #7fa860;
    --scene-grey: #6d7480;
    --badge-green: #7cc45a;
  }
  * { margin: 0; padding: 0; box-sizing: border-box; }
  html, body { width: 1200px; height: 890px; overflow: hidden; background: var(--paper); }
  .cover { position: relative; width: 1200px; height: 890px; background: var(--paper); font-family: "Cabin", sans-serif; }
  .sky-photo {
    position: absolute; left: 0; top: 251px; width: 1200px; height: 497px;
    background: linear-gradient(180deg, var(--sky-deep) 0%, #3f8ee0 45%, var(--sky-light) 100%);
  }
  .frame { position: absolute; left: 0; top: 0; width: 1200px; height: 890px; }
  .title-type { font-family: "Montserrat", sans-serif; font-weight: 600; }
  .brand-type { font-family: "Cabin", sans-serif; font-weight: 600; }
  .barcode-space {
    position: absolute; left: 338px; top: 720px; width: 215px; height: 131px;
    background: #fff; border: 1px solid #8a8a8a;
  }
  .contact {
    position: absolute; left: 39px; top: 792px;
    font-size: 14px; line-height: 15px; font-weight: 500; color: var(--ink);
    white-space: nowrap;
  }
  .subtitle {
    position: absolute; left: 640px; top: 761px; width: 540px;
    text-align: center; font-size: 28px; line-height: 30px; font-weight: 600;
    color: var(--title-green); white-space: nowrap;
  }
  .subtitle .accent { color: var(--title-red); }
</style>
</head>
<body>
<div class="cover">
  <div class="sky-photo" role="img" aria-label="Foto eines blauen Himmels mit weißen Wolken"></div>

  <svg class="frame" viewBox="0 0 1200 890" xmlns="http://www.w3.org/2000/svg">
    <defs>
      <linearGradient id="sceneTone" x1="0" y1="0" x2="0" y2="1">
        <stop offset="0" stop-color="var(--scene-green)" stop-opacity="0.75"/>
        <stop offset="0.45" stop-color="var(--scene-grey)" stop-opacity="0.8"/>
        <stop offset="1" stop-color="var(--scene-grey)" stop-opacity="0.6"/>
      </linearGradient>
      <linearGradient id="badgeTone" x1="0" y1="0" x2="0" y2="1">
        <stop offset="0" stop-color="var(--badge-green)" stop-opacity="0.8"/>
        <stop offset="1" stop-color="var(--badge-green)" stop-opacity="0.5"/>
      </linearGradient>
    </defs>

    <!-- front scene area -->
    <rect x="665" y="285" width="505" height="470" fill="url(#sceneTone)" role="img"
      aria-label="Illustration: kleiner Planet aus Müllsäcken und Plastikabfall mit Wiese, Haus und Bäumen oben und einem Reißverschluss in der Mitte"/>

    <!-- mascot area -->
    <rect x="1050" y="305" width="130" height="95" fill="url(#badgeTone)" role="img"
      aria-label="Illustration: Comicfigur mit erhobenem Daumen und Glasflasche"/>

    <!-- bands -->
    <rect x="0" y="249" width="1200" height="2.5" fill="var(--title-red)"/>
    <rect x="0" y="747" width="1200" height="2.5" fill="var(--title-red)"/>

    <!-- back cover title -->
    <text class="title-type" x="86" y="92" font-size="71" fill="var(--title-red)" textLength="420" lengthAdjust="spacing">SONNIG</text>
    <text class="title-type" x="86" y="200" font-size="112" fill="var(--title-green)" textLength="422" lengthAdjust="spacingAndGlyphs">KOCHEN</text>

    <!-- spine -->
    <circle cx="601" cy="55" r="11" fill="var(--title-green)"/>
    <text class="brand-type" font-size="26" fill="var(--title-green)" transform="translate(592 90) rotate(90)" textLength="147" lengthAdjust="spacingAndGlyphs">Wolkenheld</text>
    <text class="title-type" font-size="27" transform="translate(591 323) rotate(90)" textLength="321" lengthAdjust="spacing"><tspan fill="var(--title-red)">SONNIG </tspan><tspan fill="var(--title-green)">KOCHEN</tspan></text>

    <!-- front cover title -->
    <text class="title-type" x="638" y="107" font-size="88" fill="var(--title-red)" textLength="525" lengthAdjust="spacing">SONNIG</text>
    <text class="title-type" x="638" y="241" font-size="140" fill="var(--title-green)" textLength="527" lengthAdjust="spacingAndGlyphs">KOCHEN</text>

    <!-- challenge ribbon -->
    <g transform="translate(1100 428) rotate(16)">
      <rect x="-82" y="-22" width="164" height="44" fill="var(--title-red)" stroke="#111" stroke-width="1.5"/>
      <text x="0" y="-4" font-family="Cabin, sans-serif" font-size="12.5" font-weight="600" text-anchor="middle" fill="#111">inkl. 30 Tage</text>
      <text x="0" y="13" font-family="Cabin, sans-serif" font-size="12.5" font-weight="600" text-anchor="middle" fill="#111">Wolkenretter Challenge</text>
    </g>

    <!-- back cover brand -->
    <circle cx="120" cy="705" r="38" fill="var(--title-green)"/>
    <text class="brand-type" x="120" y="772" font-size="26" text-anchor="middle" fill="var(--title-green)">Wolkenheld</text>
  </svg>

  <div class="barcode-space"></div>

  <p class="contact">
    Wolkenheld Denke global - Handle lokal<br>
    Instagram: Wolkenheld<br>
    Webseite: wolkenheld-beispiel.de<br>
    Email: info@wolkenheld-beispiel.de
  </p>

  <p class="subtitle">Wie du durch <span class="accent">Zero Waste</span> die Umwelt<br>nachhaltig von Abfall befreist und dein<br>Leben ökologischer gestaltest</p>
</div>
</body>
</html>
```